New singe page website for our software development company

We need a single webpage that includes information about our company, contact details and a job posting. It should scroll vertically with some cool animations and parallax scrolling effects.

We are a software development consulting company that writes custom software for our customers. The webpage should have graphics and illustrations that illustrate this.

Find our logo attached, it can be modified as needed.

Thanks for all the design. When looking through the various design it's clear to us, that car related images does not look right.

We got to have software design/engineering images instead.

Our unique selling points are:

• Custom software development
• Project Managment
• Industry Services
We want these displayed with some text and icons. The icons should either have the red/brown colour from our logo, or a colour that matches the design

Software

```html
<!DOCTYPE html>
<html lang="en">
<head>
<meta charset="utf-8">
<title>BrightForge – Website Sections</title>
<link href="https://fonts.googleapis.com/css2?family=Open+Sans:wght@300;400;600;700&display=swap" rel="stylesheet">
<style>
:root{
  --red:#c0392b;
  --blue:#3d6fa8;
  --blue-soft:#5b7fae;
  --navy:#1c2740;
  --ink:#444;
  --muted:#888;
  --line:#e2e2e2;
  --panel:#f3f3f3;
  --orange:#d9693a;
  --footer:#2b2b2b;
}
*{box-sizing:border-box;margin:0;padding:0}
html,body{width:780px;height:1200px;overflow:hidden}
body{position:relative;background:#fff;font-family:"Open Sans",Arial,sans-serif;color:var(--ink)}
.section-shot{position:absolute;width:378px;height:186px;overflow:hidden;background:#fff;box-shadow:0 0 3px rgba(0,0,0,.18)}
.topbar{position:absolute;left:0;top:0;right:0;height:20px;background:#fff;border-bottom:1px solid var(--line);display:flex;align-items:center;justify-content:space-between;padding:0 8px;z-index:2}
.brand{font-size:7px;font-weight:700;color:var(--red);display:flex;align-items:center;gap:2px}
.brand::before{content:"";width:4px;height:4px;background:var(--red);border-radius:50%}
.main-nav{display:flex;gap:6px;font-size:4.4px;color:#666}
.main-nav span{position:relative}
.main-nav .active{color:var(--blue)}
.main-nav .active::after{content:"";position:absolute;left:50%;top:9px;margin-left:-3px;border:3px solid transparent;border-bottom-color:var(--blue)}
.section-title{position:absolute;left:0;right:0;text-align:center;font-weight:300;font-size:10px;color:#555}
.small{font-size:3.8px;line-height:1.5;color:var(--muted)}
.photo{position:absolute}

/* hero */
.hero-bg{position:absolute;left:0;top:20px;right:0;bottom:0;background:radial-gradient(ellipse at 60% 40%,#4a5d86,#1c2740 70%)}
.hero-devices{left:14px;top:32px;width:176px;height:130px;
  background:
    radial-gradient(circle at 30% 45%,rgba(120,200,255,.75),transparent 28%),
    radial-gradient(circle at 62% 38%,rgba(255,255,255,.55),transparent 22%),
    radial-gradient(circle at 45% 75%,rgba(220,60,50,.45),transparent 20%),
    linear-gradient(135deg,#0e1a33,#27467a 50%,#0c1428)}
.hero-card{position:absolute;left:212px;top:36px;width:140px;height:118px;background:rgba(120,135,170,.45);padding:10px;color:#fff}
.hero-card h2{font-size:8.5px;font-weight:600}
.hero-card h3{font-size:5px;font-weight:400;color:#cfd8ea;margin-bottom:4px}
.hero-card .small{color:#d7deea}
.field{height:9px;background:#fff;border:1px solid #ccc;font-size:3.8px;color:#999;padding:2px 4px;margin-top:8px}
.btn-orange{display:inline-block;background:var(--orange);color:#fff;font-size:4px;padding:3px 7px;border-radius:5px;margin:8px 0 0 22px}
.slide-arrow{position:absolute;top:95px;width:7px;height:14px;background:rgba(255,255,255,.2)}

/* outsourcing */
.dark{background:#070707}
.chalkboard{left:58px;top:72px;width:128px;height:96px;
  background:
    radial-gradient(ellipse at 70% 55%,rgba(240,240,240,.55),transparent 30%),
    radial-gradient(ellipse at 35% 40%,rgba(200,200,200,.35),transparent 40%),
    linear-gradient(160deg,#5a5d60,#34373a 60%,#1e2022)}
.out-text{position:absolute;left:205px;top:82px;width:140px;color:#bbb}
.out-text h4{font-size:5.5px;font-weight:400;margin-bottom:4px}
.out-text h4 b{color:#8fb3e4;font-weight:400}
.dot{position:absolute;left:186px;top:174px;width:4px;height:4px;border-radius:50%;background:var(--blue-soft)}

/* who we are */
.intro-box{position:absolute;left:22px;top:60px;width:334px;height:88px;background:var(--panel);border:1px solid var(--line);padding:10px 12px;text-align:center}
.intro-box h4{font-size:7.3px;font-weight:600;color:#666;line-height:1.25;margin-bottom:5px}
.fade-title{top:162px;opacity:.55;font-size:8px}

/* industries */
.industry{position:absolute;top:56px;width:104px;border:1px solid var(--line);background:#fff}
.industry h5{font-size:6px;font-weight:400;text-align:center;padding:3px 0}
.industry .banner{height:30px;background:linear-gradient(#5f86b8,#3d6fa8);color:#fff;text-align:center;border-top:3px solid #b7574a}
.industry .banner b{display:block;font-size:11px;font-weight:400;line-height:20px}
.industry .banner i{font-style:normal;font-size:3.6px}
.industry li{list-style:none;font-size:3.6px;color:#777;text-align:center;padding:3px 0;border-top:1px solid var(--line)}

/* dev services */
.title-band{position:absolute;left:22px;right:22px;top:24px;height:52px;background:var(--panel)}
.service{position:absolute;top:94px;width:100px}
.service .icon{float:left;width:11px;height:11px;background:var(--blue-soft);margin-right:3px;border-radius:2px}
.service h5{font-size:5px;font-weight:600;margin-bottom:2px}
.btn-outline{display:inline-block;margin-top:3px;border:1px solid #ccc;font-size:3.6px;padding:2px 4px;color:#666}

/* faq */
.faq-list{position:absolute;left:26px;top:76px;width:86px}
.faq-list div{font-size:3.8px;border:1px solid #cfd6e2;padding:3px 4px;margin-bottom:5px;color:#777}
.faq-list .on{background:var(--blue-soft);color:#fff;border-color:var(--blue-soft)}
.faq-answer{position:absolute;left:120px;top:76px;width:228px;height:84px;background:var(--panel);padding:7px}
.faq-answer h5{font-size:4.4px;font-weight:600;margin-bottom:3px}

/* consulting */
.consult{position:absolute;top:70px;width:78px}
.consult .photo{position:static;height:42px}
.consult h5{font-size:4.6px;font-weight:600;margin:4px 0 2px}

/* team */
.member-photo{position:absolute;top:72px;width:62px;height:62px;border-radius:50%;border:3px solid #fff;box-shadow:0 0 3px rgba(0,0,0,.25)}
.member{position:absolute;top:74px;width:84px}
.member h5{font-size:5px;font-weight:400;color:var(--orange);margin-bottom:3px}
.member h5 span{color:#666}
.socials{display:flex;gap:2px;margin-top:4px}
.socials i{width:5px;height:5px;border-radius:50%;background:var(--blue)}

/* contact */
.contact-shot{left:185px;top:863px;width:410px;height:320px}
.contact-bg{position:absolute;left:0;top:20px;right:0;height:200px;
  background:
    radial-gradient(ellipse at 25% 55%,rgba(110,140,190,.45),transparent 40%),
    radial-gradient(ellipse at 80% 30%,rgba(90,110,150,.4),transparent 35%),
    radial-gradient(ellipse at 50% 40%,#46506a,#1a1e2a 75%)}
.contact-form{position:absolute;left:88px;top:72px;width:234px;height:126px;background:rgba(255,255,255,.08);padding:8px}
.contact-form .small{color:#dde}
.row{display:flex;gap:6px;margin-top:5px}
.input{flex:1;height:9px;background:#d9dbe0;font-size:3.8px;color:#777;padding:2px 4px}
.textarea{height:50px;background:#d9dbe0;margin-top:5px;font-size:3.8px;color:#777;padding:2px 4px}
.btn-red{display:block;width:40px;margin:6px auto 0;background:#c65a46;color:#fff;font-size:4px;text-align:center;padding:2px 0;border-radius:5px}
.site-footer{position:absolute;left:0;right:0;top:220px;bottom:0;background:var(--footer);color:#aaa;display:flex;gap:14px;padding:14px 24px}
.site-footer > div{flex:1}
.site-footer h6{font-size:5px;color:#eee;font-weight:600;margin-bottom:4px}
.site-footer .brand{font-size:6.5px;margin-bottom:4px}
.site-footer .small{color:#999}
.tweet{color:var(--orange)}
.info{display:flex;align-items:center;gap:3px;margin-top:4px}
.info svg{flex:none}
</style>
</head>
<body>

<!-- Hero -->
<section class="section-shot" style="left:6px;top:12px;height:180px">
  <header class="topbar"><div class="brand">BrightForge</div><nav class="main-nav"><span class="active">Home</span><span>Who We Are</span><span>Development</span><span>Consulting</span><span>Outsourcing</span><span>Industries</span><span>Faq</span><span>Our Team</span><span>Contact</span></nav></header>
  <div class="hero-bg"></div>
  <div class="photo hero-devices" role="img" aria-label="Tablet and phone screens with a hand touching glowing app icons"></div>
  <div class="slide-arrow" style="left:0"></div><div class="slide-arrow" style="right:0"></div>
  <div class="hero-card">
    <h2>Software Development</h2>
    <h3>Ideal for Start-ups</h3>
    <p class="small">We design, build and maintain custom software for growing teams, from first idea to stable release, with clear planning and honest delivery dates.</p>
    <div class="field">Your email</div>
    <span class="btn-orange">Start Your Free Trial</span>
  </div>
</section>

<!-- Outsourcing -->
<section class="section-shot dark" style="left:392px;top:12px;height:180px">
  <header class="topbar"><div class="brand">BrightForge</div><nav class="main-nav"><span>Home</span><span>Who We Are</span><span>Development</span><span>Consulting</span><span class="active">Outsourcing</span><span>Industries</span><span>Faq</span><span>Our Team</span><span>Contact</span></nav></header>
  <h2 class="section-title" style="top:40px;color:#bbb">Software Outsourcing</h2>
  <div class="photo chalkboard" role="img" aria-label="Man drawing software diagrams on a chalkboard"></div>
  <div class="out-text">
    <h4>Upload your files. <b>Anywhere, anytime.</b></h4>
    <p class="small" style="color:#888">We offer software outsourcing services for teams of every size, with dedicated developers and steady delivery across every stage of your project.</p>
  </div>
  <span class="dot"></span>
</section>

<!-- Who We Are -->
<section class="section-shot" style="left:6px;top:198px">
  <header class="topbar"><div class="brand">BrightForge</div><nav class="main-nav"><span>Home</span><span class="active">Who We Are</span><span>Development</span><span>Consulting</span><span>Outsourcing</span><span>Industries</span><span>Faq</span><span>Our Team</span><span>Contact</span></nav></header>
  <h2 class="section-title" style="top:30px">Who We Are</h2>
  <div class="intro-box">
    <h4>Serving Our Clients with Software Development, Outsourcing and Technology Consulting Services.</h4>
    <p class="small">Our mission is to help organisations turn good ideas into working software. We plan carefully, write clean code and support every product long after launch. Our team works across many industries and brings practical experience to each project, from small tools to large business platforms, always with a clear focus on quality and results.</p>
  </div>
  <h3 class="section-title fade-title">Software Development Services</h3>
</section>

<!-- Industries -->
<section class="section-shot" style="left:392px;top:198px">
  <header class="topbar"><div class="brand">BrightForge</div><nav class="main-nav"><span>Home</span><span>Who We Are</span><span>Development</span><span>Consulting</span><span>Outsourcing</span><span class="active">Industries</span><span>Faq</span><span>Our Team</span><span>Contact</span></nav></header>
  <h2 class="section-title" style="top:30px">Industries</h2>
  <div class="industry" style="left:20px"><h5>Technology</h5><div class="banner"><b>Accelerate</b><i>Innovation</i></div><ul><li>Software Vendors</li><li>SaaS Cloud Service Providers</li><li>Software Enabled Service Providers</li></ul></div>
  <div class="industry" style="left:137px"><h5>Financial Services</h5><div class="banner"><b>Solutions</b><i>For Financial Markets and Businesses</i></div><ul><li>Asset &amp; Wealth Management</li><li>Retail Commercial Banking</li><li>Cards &amp; Payments</li></ul></div>
  <div class="industry" style="left:254px"><h5>Healthcare</h5><div class="banner"><b>Healthcare</b><i>Software for Better Care</i></div><ul><li>Providers</li><li>Payers</li><li>Healthcare Software Vendors</li></ul></div>
</section>

<!-- Development services -->
<section class="section-shot" style="left:6px;top:435px">
  <header class="topbar"><div class="brand">BrightForge</div><nav class="main-nav"><span>Home</span><span>Who We Are</span><span class="active">Development</span><span>Consulting</span><span>Outsourcing</span><span>Industries</span><span>Faq</span><span>Our Team</span><span>Contact</span></nav></header>
  <div class="title-band"></div>
  <h2 class="section-title" style="top:40px">Software Development Services</h2>
  <div class="service" style="left:22px"><span class="icon"></span><h5>Cloud Development</h5><p class="small">Many companies develop powerful solutions on cloud platforms. Our team builds secure, scalable web and desktop software, tailored to your processes and business goals.</p><span class="btn-outline">View details »</span></div>
  <div class="service" style="left:137px"><span class="icon"></span><h5>Backend Development</h5><p class="small">Our specialists have a deep understanding of server design and build robust systems that grow with your business and connect with the tools you already use.</p><span class="btn-outline">View details »</span></div>
  <div class="service" style="left:252px"><span class="icon"></span><h5>C/C++ Development</h5><p class="small">We develop fast native applications and embedded software, from system utilities to real-time processing, with careful testing and long-term maintenance.</p></div>
</section>

<!-- FAQ -->
<section class="section-shot" style="left:392px;top:435px">
  <header class="topbar"><div class="brand">BrightForge</div><nav class="main-nav"><span>Home</span><span>Who We Are</span><span>Development</span><span>Consulting</span><span>Outsourcing</span><span>Industries</span><span class="active">Faq</span><span>Our Team</span><span>Contact</span></nav></header>
  <h2 class="section-title" style="top:34px">Faq</h2>
  <div class="faq-list">
    <div class="on">What do I need to use BrightForge?</div>
    <div>How do I make a payment?</div>
    <div>How can I upgrade my subscription?</div>
    <div>How do I cancel my subscription?</div>
    <div>Where do I get help from BrightForge?</div>
  </div>
  <div class="faq-answer">
    <h5>What do I need to use BrightForge?</h5>
    <p class="small">All you need is a clear goal and a contact person on your side. We handle planning, design, development and testing, and we keep you informed at every step with short reports and regular demos of working software.</p>
    <p class="small" style="margin-top:4px">Projects start with a free call where we listen, ask questions and suggest the best way forward for your budget and timeline.</p>
  </div>
</section>

<!-- Consulting -->
<section class="section-shot" style="left:6px;top:652px;height:190px">
  <header class="topbar"><div class="brand">BrightForge</div><nav class="main-nav"><span>Home</span><span>Who We Are</span><span>Development</span><span class="active">Consulting</span><span>Outsourcing</span><span>Industries</span><span>Faq</span><span>Our Team</span><span>Contact</span></nav></header>
  <h2 class="section-title" style="top:36px">Technology Consulting Services</h2>
  <div class="consult" style="left:24px"><div class="photo" role="img" aria-label="Laptop with charts on a desk" style="background:radial-gradient(circle at 40% 50%,rgba(140,200,90,.7),transparent 35%),linear-gradient(135deg,#17233e,#3a5f9a 60%,#a9c0e0)"></div><h5>Portal Consulting Services</h5><p class="small">We plan and build team portals that make sharing documents simple and safe.</p></div>
  <div class="consult" style="left:108px"><div class="photo" role="img" aria-label="Colourful costume figure against a blue sky" style="background:radial-gradient(circle at 50% 35%,rgba(200,60,40,.8),transparent 30%),radial-gradient(circle at 50% 75%,rgba(220,150,60,.8),transparent 35%),linear-gradient(#4f86c6,#2f5c96)"></div><h5>Cloud Platform Consulting Services</h5><p class="small">Migration, hosting and storage set up for reliable cloud applications.</p></div>
  <div class="consult" style="left:192px"><div class="photo" role="img" aria-label="Person working at a computer in a purple lit office" style="background:radial-gradient(circle at 60% 45%,rgba(230,80,120,.7),transparent 30%),linear-gradient(135deg,#1f35a0,#5b3fa8 55%,#2b1f6a)"></div><h5>CRM Platform Consulting Services</h5><p class="small">Configure, customise and connect your customer records with ease.</p></div>
  <div class="consult" style="left:276px"><div class="photo" role="img" aria-label="Bright server room corridor" style="background:radial-gradient(ellipse at 50% 50%,#ffffff,transparent 30%),linear-gradient(90deg,#7d9cc2,#dfe9f4 50%,#7d9cc2)"></div><h5>SQL Consulting Services</h5><p class="small">Database design, tuning and reporting for fast and accurate data.</p></div>
</section>

<!-- Team -->
<section class="section-shot" style="left:392px;top:652px;height:190px">
  <header class="topbar"><div class="brand">BrightForge</div><nav class="main-nav"><span>Home</span><span>Who We Are</span><span>Development</span><span>Consulting</span><span>Outsourcing</span><span>Industries</span><span>Faq</span><span class="active">Our Team</span><span>Contact</span></nav></header>
  <h2 class="section-title" style="top:34px">Our Team</h2>
  <div class="member-photo" role="img" aria-label="Portrait of designer Sam Hale in a blue shirt" style="left:34px;background:radial-gradient(circle at 50% 85%,#3f78c8,#2a5aa0 30%,transparent 55%),linear-gradient(#f4f6f9,#cfd9e6)"></div>
  <div class="member" style="left:102px"><h5>Sam Hale <span>/ Designer</span></h5><p class="small">Sam shapes clear, friendly interfaces and turns complex workflows into screens people enjoy using every day.</p><div class="socials"><i></i><i></i><i></i><i></i></div></div>
  <div class="member-photo" role="img" aria-label="Portrait of developer Nora Pike in a dark suit" style="left:200px;background:radial-gradient(circle at 50% 90%,#1c1c1c,#2e2e2e 30%,transparent 55%),linear-gradient(#ffffff,#e6e6e6)"></div>
  <div class="member" style="left:268px"><h5>Nora Pike <span>/ Developer</span></h5><p class="small">Nora writes solid, well tested code and leads our backend work on data heavy business applications.</p><div class="socials"><i></i><i></i><i></i><i></i></div></div>
</section>

<!-- Contact -->
<section class="section-shot contact-shot">
  <header class="topbar"><div class="brand">BrightForge</div><nav class="main-nav"><span>Home</span><span>Who We Are</span><span>Development</span><span>Consulting</span><span>Outsourcing</span><span>Industries</span><span>Faq</span><span>Our Team</span><span class="active">Contact</span></nav></header>
  <div class="contact-bg" role="img" aria-label="Blurred office background"></div>
  <h2 class="section-title" style="top:48px;color:#eee">Get In Touch</h2>
  <form class="contact-form">
    <p class="small">Tell us about your project and we will reply within one business day.</p>
    <div class="row"><div class="input">Your name</div><div class="input">Your email</div></div>
    <div class="textarea">Your message</div>
    <span class="btn-red">Send Message</span>
  </form>
  <footer class="site-footer">
    <div><div class="brand">BrightForge</div><p class="small">We build custom software, manage projects end to end and support clients across many industries with steady, friendly service.</p><div class="socials" style="margin-top:6px"><i></i><i></i><i></i><i></i></div></div>
    <div><h6>Latest Tweets</h6><p class="small"><span class="tweet">@brightforge</span> New case study on cloud migration is live now.</p><p class="small" style="margin-top:4px"><span class="tweet">@brightforge</span> We are hiring a senior developer, join us.</p></div>
    <div><h6>Contact Info</h6><p class="small">Reach us by phone, email or visit our studio.</p>
      <div class="info small"><svg width="5" height="5" viewBox="0 0 10 10"><path d="M2 1l2 2-1 1.5a6 6 0 0 0 2.5 2.5L7 6l2 2-1.5 1.5C4 9 1 6 .5 2z" fill="#aaa"/></svg>(555) 014-2290</div>
      <div class="info small"><svg width="5" height="5" viewBox="0 0 10 10"><rect x="1" y="2" width="8" height="6" fill="none" stroke="#aaa"/><path d="M1 2l4 3 4-3" fill="none" stroke="#aaa"/></svg>hello@brightforge.example</div>
      <div class="info small"><svg width="5" height="5" viewBox="0 0 10 10"><path d="M5 1a3 3 0 0 1 3 3c0 2-3 5-3 5S2 6 2 4a3 3 0 0 1 3-3z" fill="#aaa"/></svg>120 Harbor Lane, Suite 4, Lakeview</div>
    </div>
  </footer>
</section>

</body>
</html>
```